Business card and stationery
Clear Harbour
Project: Business card and stationery
Business card and stationery  -
Creative Brief
Simple
Name Surname
Executive Director
317 Larkmoor Lane, #03 Fenwick Plaza, Country 264519
vantolemu@mailpost.example
www.clearharbour.example.sg
info (name, address, email etc) on the card should be editable for each employee

```html
<!DOCTYPE html>
<html lang="en">
<head>
<meta charset="utf-8">
<title>Clear Harbour — Business Card</title>
<link rel="stylesheet" href="https://fonts.googleapis.com/css2?family=Open+Sans:wght@400;600;700&display=swap">
<style>
  :root {
    --backdrop: #ebe6de;
    --card: #ffffff;
    --card-shade: #f1f1f1;
    --brand-blue: #1f6fd6;
    --brand-green: #2db31f;
    --ink: #333333;
    --ink-soft: #555555;
    --rule: #c9c9c9;
  }
  * { box-sizing: border-box; margin: 0; padding: 0; }
  html, body { width: 1200px; height: 581px; overflow: hidden; }
  body {
    background: var(--backdrop);
    font-family: "Open Sans", Arial, sans-serif;
    position: relative;
  }
  .card {
    position: absolute;
    top: 180px;
    width: 468px;
    height: 324px;
    border-radius: 14px;
    background: linear-gradient(180deg, var(--card) 60%, var(--card-shade) 100%);
    box-shadow: 0 3px 8px rgba(0,0,0,0.28);
    overflow: hidden;
  }
  .card--front { left: 96px; }
  .card--back { left: 605px; }

  .brand-name {
    color: var(--brand-blue);
    font-weight: 600;
    letter-spacing: -0.5px;
    white-space: nowrap;
  }
  .front-brand {
    position: absolute;
    left: 0;
    width: 266px;
    top: 140px;
    text-align: center;
    font-size: 29px;
  }
  .divider {
    position: absolute;
    left: 266px;
    top: 30px;
    width: 1px;
    height: 245px;
    background: var(--rule);
  }
  .contact {
    position: absolute;
    left: 280px;
    top: 36px;
    width: 176px;
    color: var(--ink);
  }
  .contact__name {
    color: var(--brand-blue);
    font-size: 18px;
    font-weight: 700;
    line-height: 1.1;
    white-space: nowrap;
  }
  .contact__role {
    font-size: 10.5px;
    font-weight: 600;
    color: var(--ink-soft);
    margin-top: 2px;
  }
  .contact__address {
    font-size: 10.5px;
    line-height: 1.55;
    margin-top: 26px;
    color: var(--ink-soft);
  }
  .contact__list {
    list-style: none;
    margin-top: 16px;
    font-size: 10px;
    color: var(--ink-soft);
  }
  .contact__list li {
    display: flex;
    align-items: center;
    gap: 7px;
    height: 20px;
    white-space: nowrap;
  }
  .contact__list svg { width: 11px; height: 11px; flex: none; }

  .band {
    position: absolute;
    left: 0;
    bottom: 20px;
    width: 468px;
    height: 14px;
  }

  .back-brand {
    position: absolute;
    left: 0;
    width: 100%;
    top: 132px;
    text-align: center;
    font-size: 34px;
  }
  .back-web {
    position: absolute;
    left: 0;
    width: 100%;
    bottom: 30px;
    text-align: center;
    font-size: 14px;
    font-weight: 600;
    color: var(--ink-soft);
  }
</style>
</head>
<body>

<section class="card card--front">
  <div class="brand-name front-brand">Clear Harbour</div>
  <div class="divider"></div>
  <div class="contact">
    <p class="contact__name">Name Surname</p>
    <p class="contact__role">Executive Director</p>
    <p class="contact__address">317 Larkmoor Lane,<br>#03 Fenwick Plaza,<br>Country 264519</p>
    <ul class="contact__list">
      <li>
        <svg viewBox="0 0 12 12" aria-hidden="true"><path d="M2.5 1 L4.5 1 L5.3 3.4 L4 4.4 Q5 6.8 7.6 8 L8.6 6.7 L11 7.5 L11 9.5 Q10.5 11 9 11 Q1 10 1 2.8 Q1 1 2.5 1 Z" fill="var(--brand-blue)"/></svg>
        <span>+77 5550 0141</span>
      </li>
      <li>
        <svg viewBox="0 0 12 12" aria-hidden="true"><rect x="3" y="0.5" width="6" height="11" rx="1.2" fill="var(--brand-blue)"/><rect x="4" y="2" width="4" height="6.5" fill="#fff"/></svg>
        <span>+88 5550 0192</span>
      </li>
      <li>
        <svg viewBox="0 0 12 12" aria-hidden="true"><circle cx="6" cy="6" r="2.2" fill="none" stroke="var(--brand-blue)" stroke-width="1.4"/><path d="M8.2 4 V7 Q8.2 8.6 9.5 8.6 Q11 8.6 11 6 A5 5 0 1 0 8.5 10.3" fill="none" stroke="var(--brand-blue)" stroke-width="1.4"/></svg>
        <span>vantolemu@mailpost.example</span>
      </li>
      <li>
        <svg viewBox="0 0 12 12" aria-hidden="true"><circle cx="6" cy="6" r="5" fill="none" stroke="var(--brand-blue)" stroke-width="1.2"/><ellipse cx="6" cy="6" rx="2.2" ry="5" fill="none" stroke="var(--brand-blue)" stroke-width="1"/><line x1="1" y1="6" x2="11" y2="6" stroke="var(--brand-blue)" stroke-width="1"/></svg>
        <span>www.clearharbour.example.sg</span>
      </li>
    </ul>
  </div>
  <svg class="band" viewBox="0 0 468 14" preserveAspectRatio="none" aria-hidden="true">
    <polygon points="0,0 352,0 340,14 0,14" fill="var(--brand-blue)"/>
    <polygon points="358,0 468,0 468,14 346,14" fill="var(--brand-green)"/>
  </svg>
</section>

<section class="card card--back">
  <div class="brand-name back-brand">Clear Harbour</div>
  <p class="back-web">www.clearharbour.example.sg</p>
</section>

</body>
</html>
```